Direct Mail Postcard for new client solicitation

I need a postcard designed to market our full service accounting and financial services firm to local companies.

Our firm specializes in outsourced accounting and finance - we do everything from book keeping all the way up to financial oversight. We prefer to work on a flat fee recurring revenue basis rather than a traditional hourly fee. We also bring our own privately developed software to assist with the process. This software is proprietary in nature and not available elsewhere.

This card should convey:
1. Transferring financial headaches to a qualified company.
2. Stable access to help.
3. Cost savings.
4. A comprehensive package that allows for the client to take as much or as little as they would like.

I have attached our logo as a starting point. Feel free to engage us with questions and for guidance.

The company name is BrightLedgerPro.

Target Market(s)

the target market for this project is small businesses in the chicago area (our test market) with annual revenues between 5 and 10 Million dollars

Industry/Entity Type

Accounting

Font styles to use
Serif
Sans Serif

Requirements
Must have
• The project must convey the idea that we are taking administrative burdens and headaches from the client. The idea is that they are outsourcing their back office accounting functions to us while still retaining overall control of the process. The card must convey this concept somehow.
• We are also working on copy - since we are accountants and basically as boring as watching paint dry we are struggling a bit. Feel free to take a stab at copy as well. Keep in mind - we do not need to say alot - ideally we would say in essence "outsource your finance and accounting work to us for a reasonable fixed price".
Should not have
• We are reworking our website as well. The little orange guys and in fact the entire copy will be changing over the next few weeks. We would prefer to avoid using that motif for the card.

```html
<!DOCTYPE html>
<html lang="en">
<head>
<meta charset="utf-8">
<title>BrightLedgerPro Postcard</title>
<link href="https://fonts.googleapis.com/css2?family=Open+Sans:wght@300;400;600;700&family=PT+Serif:ital@1&display=swap" rel="stylesheet">
<style>
  :root {
    --page: #e9e9e9;
    --sky: #bfe4f8;
    --sky-soft: #d9effb;
    --brand-blue: #1a7fc0;
    --panel: #f1f1f1;
    --ink: #1b1b1b;
    --body-grey: #555;
    --line: #9a9a9a;
    --white: #ffffff;
    --photo-a: #c9d3dc;
    --photo-b: #6d86a6;
  }
  * { box-sizing: border-box; margin: 0; padding: 0; }
  html, body { width: 1057px; height: 1200px; overflow: hidden; }
  body { background: var(--page); font-family: "Open Sans", Arial, sans-serif; color: var(--ink); position: relative; }

  .postcard { position: absolute; background: var(--white); overflow: hidden; box-shadow: 0 3px 10px rgba(0,0,0,.18); }
  .postcard--front { left: 67px; top: 56px; width: 831px; height: 539px; }
  .postcard--back { left: 137px; top: 631px; width: 829px; height: 538px; }

  .header { position: absolute; left: 0; top: 0; width: 100%; height: 140px; background: var(--sky); }
  .header__swoosh { position: absolute; left: 0; bottom: 0; width: 100%; height: 40px; }
  .headline { position: absolute; font-family: "PT Serif", Georgia, serif; font-style: italic; color: var(--ink); }
  .postcard--front .headline { left: 31px; top: 28px; font-size: 25px; line-height: 31px; }
  .postcard--back .headline { left: 39px; top: 32px; font-size: 20px; line-height: 28px; }

  .brand { position: absolute; display: flex; align-items: center; gap: 10px; }
  .brand__name { font-family: "Open Sans", Arial, sans-serif; font-weight: 700; font-size: 27px; letter-spacing: -0.5px; color: var(--ink); }
  .brand__mark { width: 34px; height: 34px; background: var(--brand-blue); }
  .postcard--front .brand { left: 545px; top: 47px; }
  .postcard--back .brand { left: 540px; top: 46px; }

  .hero-photo { position: absolute; left: 0; top: 135px; width: 503px; height: 376px;
    background: linear-gradient(160deg, var(--photo-a) 0%, var(--photo-b) 55%, #e8ecef 100%); }

  .services { position: absolute; left: 503px; top: 175px; width: 320px; height: 336px; background: var(--panel); }
  .services__tab { position: absolute; left: 492px; top: 119px; width: 325px; height: 66px; background: var(--brand-blue);
    border-radius: 6px; color: var(--white); font-size: 25px; font-weight: 400; display: flex; align-items: center; justify-content: center; }
  .services__list { position: absolute; left: 520px; top: 204px; list-style: none; font-size: 17px; line-height: 23.3px; color: var(--ink); }
  .services__list li { display: flex; align-items: center; gap: 7px; }
  .tick { width: 13px; height: 13px; flex: none; }

  .tagline { position: absolute; font-weight: 700; color: var(--ink); white-space: nowrap; }
  .postcard--front .tagline { left: 510px; top: 441px; font-size: 15.5px; }
  .postcard--back .tagline { left: 0; width: 500px; text-align: center; top: 342px; font-size: 18px; }

  .contact { position: absolute; display: flex; align-items: center; gap: 7px; color: var(--brand-blue); white-space: nowrap; }
  .contact__label { font-weight: 400; }
  .contact__phone { font-weight: 600; }
  .phone-icon { flex: none; }
  .postcard--front .contact { left: 510px; top: 482px; font-size: 17px; }
  .postcard--back .contact { left: 68px; top: 380px; font-size: 21px; gap: 11px; }

  .footer-bar { position: absolute; left: 0; bottom: 0; width: 100%; height: 29px; background: var(--brand-blue); }

  .about-panel { position: absolute; left: 0; top: 135px; width: 480px; height: 285px; background: var(--panel);
    border-right: 1px solid #ccc; border-bottom: 1px solid #ccc; border-bottom-right-radius: 10px; }
  .about-copy { position: absolute; left: 38px; top: 183px; width: 411px; font-size: 12.4px; line-height: 17.4px;
    color: var(--body-grey); text-align: justify; }
  .web-pill { position: absolute; left: 60px; top: 420px; width: 367px; height: 42px; background: var(--brand-blue);
    border-radius: 0 0 20px 20px; color: var(--white); font-size: 24px; letter-spacing: 1px;
    display: flex; align-items: center; justify-content: center; }

  .stamp-box { position: absolute; left: 730px; top: 137px; width: 66px; height: 54px; border: 1px solid var(--line); }
  .address-line { position: absolute; left: 591px; width: 203px; height: 1px; background: var(--line); }
</style>
</head>
<body>

<section class="postcard postcard--front">
  <header class="header">
    <svg class="header__swoosh" viewBox="0 0 831 40" preserveAspectRatio="none">
      <path d="M0 14 Q420 34 831 8 L831 40 L0 40 Z" fill="#ffffff"/>
      <path d="M0 4 Q300 30 700 20 Q360 26 0 14 Z" fill="#d9effb"/>
    </svg>
    <p class="headline">FINALLY - a way to outsource those financial<br>headaches without losing control!</p>
    <div class="brand"><span class="brand__name">BrightLedgerPro</span><span class="brand__mark"></span></div>
  </header>

  <div class="hero-photo" role="img" aria-label="Stressed man at a desk holding his head among papers, books, glasses and a calculator"></div>

  <div class="services"></div>
  <div class="services__tab">We can help with:</div>
  <ul class="services__list">
    <li><svg class="tick" viewBox="0 0 14 14"><circle cx="7" cy="7" r="7" fill="#1a7fc0"/><path d="M3.8 7.2 6 9.3 10.2 4.9" stroke="#fff" stroke-width="1.8" fill="none"/></svg>Financial management</li>
    <li><svg class="tick" viewBox="0 0 14 14"><circle cx="7" cy="7" r="7" fill="#1a7fc0"/><path d="M3.8 7.2 6 9.3 10.2 4.9" stroke="#fff" stroke-width="1.8" fill="none"/></svg>Accounting</li>
    <li><svg class="tick" viewBox="0 0 14 14"><circle cx="7" cy="7" r="7" fill="#1a7fc0"/><path d="M3.8 7.2 6 9.3 10.2 4.9" stroke="#fff" stroke-width="1.8" fill="none"/></svg>Book keeping</li>
    <li><svg class="tick" viewBox="0 0 14 14"><circle cx="7" cy="7" r="7" fill="#1a7fc0"/><path d="M3.8 7.2 6 9.3 10.2 4.9" stroke="#fff" stroke-width="1.8" fill="none"/></svg>Forecasting</li>
    <li><svg class="tick" viewBox="0 0 14 14"><circle cx="7" cy="7" r="7" fill="#1a7fc0"/><path d="M3.8 7.2 6 9.3 10.2 4.9" stroke="#fff" stroke-width="1.8" fill="none"/></svg>Reporting</li>
    <li><svg class="tick" viewBox="0 0 14 14"><circle cx="7" cy="7" r="7" fill="#1a7fc0"/><path d="M3.8 7.2 6 9.3 10.2 4.9" stroke="#fff" stroke-width="1.8" fill="none"/></svg>Bank management</li>
    <li><svg class="tick" viewBox="0 0 14 14"><circle cx="7" cy="7" r="7" fill="#1a7fc0"/><path d="M3.8 7.2 6 9.3 10.2 4.9" stroke="#fff" stroke-width="1.8" fill="none"/></svg>Fund raising</li>
    <li><svg class="tick" viewBox="0 0 14 14"><circle cx="7" cy="7" r="7" fill="#1a7fc0"/><path d="M3.8 7.2 6 9.3 10.2 4.9" stroke="#fff" stroke-width="1.8" fill="none"/></svg>Business transition planning</li>
    <li><svg class="tick" viewBox="0 0 14 14"><circle cx="7" cy="7" r="7" fill="#1a7fc0"/><path d="M3.8 7.2 6 9.3 10.2 4.9" stroke="#fff" stroke-width="1.8" fill="none"/></svg>Tax compliance</li>
  </ul>
  <p class="tagline">If you have headaches WE have solutions!</p>
  <div class="contact">
    <span class="contact__label">Contact Us</span>
    <svg class="phone-icon" width="21" height="21" viewBox="0 0 22 22"><circle cx="11" cy="11" r="9.5" fill="none" stroke="#1a7fc0" stroke-width="2"/><path d="M7.3 5.8c.6-.5 1.3-.4 1.6.2l1 1.9c.3.5.1 1-.3 1.3l-.7.5c.6 1.4 1.6 2.5 3 3.2l.6-.7c.4-.4 1-.5 1.4-.2l1.8 1.1c.5.3.6 1 .1 1.6-.8.9-1.9 1.2-3 .8-3-1.2-5-3.4-5.9-6.3-.3-1.2 0-2.5.4-3.4z" fill="#1a7fc0"/></svg>
    <span class="contact__phone">855-555-BLPR (2577)</span>
  </div>
  <div class="footer-bar"></div>
</section>

<section class="postcard postcard--back">
  <header class="header">
    <svg class="header__swoosh" viewBox="0 0 829 40" preserveAspectRatio="none">
      <path d="M0 20 Q420 32 829 0 L829 40 L0 40 Z" fill="#ffffff"/>
      <path d="M0 6 Q300 28 690 22 Q360 30 0 20 Z" fill="#d9effb"/>
    </svg>
    <p class="headline">Outsource your finance and accounting work to us<br>for a reasonable fixed price!</p>
    <div class="brand"><span class="brand__name">BrightLedgerPro</span><span class="brand__mark"></span></div>
  </header>

  <div class="about-panel"></div>
  <p class="about-copy">BrightLedgerPro is more than a consulting firm – we are a partner that provides a total solution for all your financial headaches. BrightLedgerPro is a revolutionary way to handle your business finances. Using proprietary tools that allow you to control and monitor the processing of data we provide the most comprehensive solution to all your accounting and finance issues! Now you can move just the issues you want - at prices you can afford.</p>
  <p class="tagline">If you have headaches WE have solutions!</p>
  <div class="contact">
    <span class="contact__label">Contact Us</span>
    <svg class="phone-icon" width="25" height="25" viewBox="0 0 22 22"><circle cx="11" cy="11" r="9.5" fill="none" stroke="#1a7fc0" stroke-width="2"/><path d="M7.3 5.8c.6-.5 1.3-.4 1.6.2l1 1.9c.3.5.1 1-.3 1.3l-.7.5c.6 1.4 1.6 2.5 3 3.2l.6-.7c.4-.4 1-.5 1.4-.2l1.8 1.1c.5.3.6 1 .1 1.6-.8.9-1.9 1.2-3 .8-3-1.2-5-3.4-5.9-6.3-.3-1.2 0-2.5.4-3.4z" fill="#1a7fc0"/></svg>
    <span class="contact__phone">855-555-BLPR (2577)</span>
  </div>
  <div class="web-pill">www.brightledgerpro.com</div>

  <div class="stamp-box"></div>
  <div class="address-line" style="top:251px"></div>
  <div class="address-line" style="top:289px"></div>
  <div class="address-line" style="top:327px"></div>

  <div class="footer-bar"></div>
</section>

</body>
</html>
```